Moving comapny Postcard mailer Design

I am looking for a 6x9 postcard with real images of our team. I would like to add the same review we currently have , I want the colors of the postcard to be orange and white. I want the team picture to be enlarged with the other pictures to be mimized. I will add example postcards to give rough ideas. My company is called Harlow Moving and the postcards with that name are our current postcards. The additional postcards are from other companies who have better postcards than mine. My goal is for my postcard to be better that theirs.

Target Market(s)

Wealthy people in the 35+ age group

Industry/Entity Type

Moving company

Requirements
Must have
• Beauty

```html
<!DOCTYPE html>
<html lang="en">
<head>
<meta charset="utf-8">
<title>Harlow Moving Postcard</title>
<link rel="stylesheet" href="https://fonts.googleapis.com/css2?family=Arimo:ital,wght@0,400;0,700;1,400&family=Montserrat:ital,wght@0,700;0,800;0,900;1,900&display=swap">
<style>
  :root {
    --orange: #e2502a;
    --white: #ffffff;
    --ink: #1c1c1c;
    --badge: #3a3a3a;
    --star: #f2b632;
    --photo-dark: #3d4434;
    --photo-mid: #6d7a5c;
    --photo-light: #aeb8a8;
    --faded: #eef0f1;
  }
  * { margin: 0; padding: 0; box-sizing: border-box; }
  html, body { width: 1200px; height: 800px; overflow: hidden; background: var(--white); }
  .postcard {
    position: relative;
    width: 1200px;
    height: 800px;
    background: var(--white);
    font-family: "Arimo", Arial, sans-serif;
    color: var(--ink);
    overflow: hidden;
  }
  .faded-truck {
    position: absolute;
    left: 380px; top: 150px;
    width: 230px; height: 330px;
    background: linear-gradient(90deg, rgba(238,240,241,0) 0%, var(--faded) 45%, #e4e7e9 100%);
  }
  .headline {
    position: absolute;
    left: 60px; top: 38px;
    font-family: "Montserrat", sans-serif;
    font-weight: 900;
    font-style: italic;
    font-size: 98px;
    line-height: 97px;
    letter-spacing: -1px;
    color: var(--orange);
    text-transform: uppercase;
  }
  .brand-mark {
    position: absolute;
    left: 190px; top: 320px;
    width: 230px;
    display: flex;
    align-items: center;
    gap: 12px;
    font-family: "Montserrat", sans-serif;
    font-weight: 900;
    font-size: 26px;
    color: var(--orange);
    text-transform: uppercase;
    line-height: 1.1;
  }
  .brand-mark .square {
    width: 40px; height: 40px;
    flex: none;
    background: var(--orange);
  }
  .stars {
    position: absolute;
    left: 222px; top: 461px;
    display: flex; gap: 4px;
  }
  .review {
    position: absolute;
    left: 40px; top: 490px;
    width: 525px;
    text-align: center;
    font-size: 18px;
    line-height: 23.5px;
    color: var(--ink);
  }
  .dot-number {
    position: absolute;
    left: 240px; top: 639px;
    width: 124px; height: 26px;
    background: var(--badge);
    color: var(--white);
    font-size: 13px;
    line-height: 26px;
    text-align: center;
  }
  .team-photo {
    position: absolute;
    left: 600px; top: 0;
    width: 600px; height: 558px;
    background: linear-gradient(180deg, var(--photo-mid) 0%, var(--photo-dark) 45%, #555a5a 80%, #6f7273 100%);
  }
  .offers { position: absolute; left: 612px; top: 534px; }
  .offer {
    position: absolute;
    top: 0;
    width: 181px; height: 126px;
    background: var(--orange);
    color: var(--white);
    text-align: center;
  }
  .offer::before {
    content: "";
    position: absolute; inset: 6px;
    border: 1.5px dashed var(--white);
  }
  .offer:nth-child(1) { left: 0; }
  .offer:nth-child(2) { left: 193px; }
  .offer:nth-child(3) { left: 388px; }
  .offer-amount {
    margin-top: 20px;
    font-family: "Montserrat", sans-serif;
    font-weight: 900;
    font-size: 30px;
    line-height: 32px;
    letter-spacing: -0.5px;
  }
  .offer-amount sup { font-size: 16px; vertical-align: 12px; }
  .offer-terms {
    margin-top: 6px;
    font-size: 18px;
    line-height: 20px;
    text-transform: uppercase;
  }
  .offer-terms .limit { text-transform: none; }
  .offer-note {
    font-size: 12px;
    font-style: italic;
    opacity: 0.85;
    margin-top: 2px;
  }
  .call-band {
    position: absolute;
    left: 0; top: 687px;
    width: 1200px; height: 79px;
    background: var(--orange);
    color: var(--white);
    display: flex;
    align-items: center;
    padding-left: 40px;
  }
  .call-band .prompt {
    font-family: "Arimo", sans-serif;
    font-style: italic;
    font-size: 31px;
    margin-right: 18px;
  }
  .call-band .phone, .call-band .web {
    display: flex; align-items: center; gap: 6px;
    font-family: "Montserrat", sans-serif;
    font-weight: 800;
  }
  .call-band .phone { font-size: 33px; margin-right: 24px; }
  .call-band .web { font-size: 30px; }
</style>
</head>
<body>
<div class="postcard">
  <div class="faded-truck" role="img" aria-label="Faded photo of a moving truck"></div>

  <h1 class="headline">Harlow<br>Moving</h1>

  <div class="brand-mark"><span class="square"></span><span>Harlow Moving</span></div>

  <div class="stars" aria-label="Five stars">
    <svg width="180" height="30" viewBox="0 0 180 30">
      <g fill="var(--star)" stroke="#c98a12" stroke-width="1">
        <polygon points="15,1 19,11 29,11 21,17 24,28 15,21 6,28 9,17 1,11 11,11"/>
        <polygon transform="translate(36 0)" points="15,1 19,11 29,11 21,17 24,28 15,21 6,28 9,17 1,11 11,11"/>
        <polygon transform="translate(72 0)" points="15,1 19,11 29,11 21,17 24,28 15,21 6,28 9,17 1,11 11,11"/>
        <polygon transform="translate(108 0)" points="15,1 19,11 29,11 21,17 24,28 15,21 6,28 9,17 1,11 11,11"/>
        <polygon transform="translate(144 0)" points="15,1 19,11 29,11 21,17 24,28 15,21 6,28 9,17 1,11 11,11"/>
      </g>
    </svg>
  </div>

  <p class="review">“This company is incredible! After working all day, they came to our house and without skipping a beat began effieciently moving our heavy household items. They had a great attitude, very friendly, and clearly enhoyed working with each other! They took extremely good care of my house hold items. Thank you for a great expereince!”</p>

  <div class="dot-number">DOT# 4820716</div>

  <div class="team-photo" role="img" aria-label="Team photo of the moving crew in black shirts standing in front of a box truck"></div>

  <div class="offers">
    <div class="offer">
      <div class="offer-amount"><sup>$</sup>25 OFF</div>
      <div class="offer-terms">Moves under<br>$1000</div>
      <div class="offer-note">With this card.</div>
    </div>
    <div class="offer">
      <div class="offer-amount"><sup>$</sup>50 OFF</div>
      <div class="offer-terms">Moves under<br>$1000</div>
      <div class="offer-note">*With this card.</div>
    </div>
    <div class="offer">
      <div class="offer-amount"><sup>$</sup>100 OFF</div>
      <div class="offer-terms">Moves under<br>$3000</div>
      <div class="offer-note">*With this card.</div>
    </div>
  </div>

  <div class="call-band">
    <span class="prompt">Call us today to get started!</span>
    <span class="phone">
      <svg width="26" height="34" viewBox="0 0 26 34" fill="none" stroke="var(--white)" stroke-width="2.5" stroke-linejoin="round">
        <path d="M6 3 L11 3 L13 10 L9 13 C10 19 13 23 17 26 L20 22 L25 25 L24 31 C14 32 3 20 3 7 Z"/>
      </svg>
      (865) 555-0142
    </span>
    <span class="web">
      <svg width="36" height="36" viewBox="0 0 36 36" fill="none" stroke="var(--white)" stroke-width="2.2">
        <circle cx="16" cy="16" r="13"/>
        <ellipse cx="16" cy="16" rx="6" ry="13"/>
        <line x1="3" y1="16" x2="29" y2="16"/>
        <path d="M21 21 L33 26 L28 28 L26 33 Z" fill="var(--white)"/>
      </svg>
      www.harlowmovers.com
    </span>
  </div>
</div>
</body>
</html>
```